CLEVER, EYE catching stationary for oil & gas technology company
Kelvor Subsurface Group
I need double sided standard sized Business Card [3.5" x 2"]
eurostile LT ExtendedTwo
Simple
Darren Holloway
Managing Partner
#22, 4307 - 3rd Avenue
Tarrowby, KV
R4K 2M9
darren.holloway@kelvor.ca
www.kelvor.ca
Business cards will have rounded corners.
Back of business card we would like to see the Kelvor logo on a black back ground (but are open to other suggestions)
Centered on the back bottom part of card it should state: "Kelvor Subsurface Group Inc."

```html
<!DOCTYPE html>
<html lang="en">
<head>
<meta charset="utf-8">
<title>Kelvor Subsurface Group – Business Card</title>
<link rel="stylesheet" href="https://fonts.googleapis.com/css2?family=Michroma&display=swap">
<style>
  :root {
    --page-bg: #e9e6e2;
    --card-white: #ffffff;
    --orange-light: #f07a3a;
    --orange-dark: #d9531c;
    --brand-orange: #e8561b;
    --brand-blue: #1e88d6;
    --stripe-blue: #2a8fdb;
    --text-light: #ffe3d2;
    --text-white: #ffffff;
    --icon-dark: #4a2a1a;
  }
  * { box-sizing: border-box; margin: 0; padding: 0; }
  html, body {
    width: 1200px; height: 900px; overflow: hidden;
    background: var(--page-bg);
    font-family: "Michroma", "Eurostile", sans-serif;
  }
  .canvas {
    width: 1200px; height: 900px;
    display: flex; align-items: center; justify-content: center;
  }
  .business-card {
    position: relative;
    width: 1000px; height: 572px;
    border-radius: 28px;
    overflow: hidden;
    background: var(--card-white);
    box-shadow: 0 10px 30px rgba(0,0,0,0.18);
  }
  .brand {
    position: absolute; top: 92px; left: 0; right: 0;
    display: flex; align-items: center; justify-content: center; gap: 16px;
  }
  .brand-dot {
    width: 30px; height: 30px; border-radius: 50%;
    background: var(--brand-blue);
  }
  .brand-name {
    font-size: 30px; color: var(--brand-orange);
    letter-spacing: 1px; text-transform: uppercase;
  }
  .info-band {
    position: absolute; left: 0; right: 0; top: 240px; height: 270px;
    background: radial-gradient(ellipse at 55% 40%, var(--orange-light), var(--orange-dark) 85%);
  }
  .band-pointer {
    position: absolute; left: 70px; top: -1px;
  }
  .blue-stripe {
    position: absolute; left: 0; right: 0; top: 518px; bottom: 0;
    background: var(--stripe-blue);
  }
  .person {
    position: absolute; left: 70px; top: 60px;
    color: var(--text-light); text-transform: uppercase;
  }
  .person-name { font-size: 16px; letter-spacing: 1px; }
  .person-title { font-size: 12px; letter-spacing: 1px; margin-top: 8px; }
  .contact-list {
    position: absolute; left: 560px; top: 28px;
    list-style: none; color: var(--text-white);
  }
  .contact-item {
    display: flex; align-items: center; gap: 12px;
    font-size: 14px; letter-spacing: 1px; line-height: 1;
    height: 34px;
  }
  .contact-item.address-line { padding-left: 34px; height: 28px; }
  .contact-icon { width: 22px; height: 22px; flex: none; }
</style>
</head>
<body>
<main class="canvas">
  <article class="business-card">
    <header class="brand">
      <span class="brand-dot"></span>
      <span class="brand-name">Kelvor Subsurface Group</span>
    </header>

    <section class="info-band">
      <svg class="band-pointer" width="36" height="22" viewBox="0 0 36 22">
        <polygon points="0,0 36,0 8,22" fill="#ffffff"/>
      </svg>

      <div class="person">
        <p class="person-name">Darren Holloway</p>
        <p class="person-title">Managing Partner</p>
      </div>

      <ul class="contact-list">
        <li class="contact-item">
          <svg class="contact-icon" viewBox="0 0 22 22"><circle cx="11" cy="11" r="11" fill="var(--icon-dark)"/><path d="M11 5a4 4 0 0 0-4 4c0 3 4 8 4 8s4-5 4-8a4 4 0 0 0-4-4z" fill="#fff"/><circle cx="11" cy="9" r="1.5" fill="var(--icon-dark)"/></svg>
          <span>#22, 4307 - 3rd Avenue</span>
        </li>
        <li class="contact-item address-line"><span>Tarrowby, KV R4K 2M9</span></li>
        <li class="contact-item">
          <svg class="contact-icon" viewBox="0 0 22 22"><circle cx="11" cy="11" r="11" fill="var(--icon-dark)"/><path d="M8 5l2 3-1.3 1.3a7 7 0 0 0 3.9 3.9L14 12l3 2-1 2.5c-4 0-9.5-5.5-9.5-9.5z" fill="#fff"/></svg>
          <span>555-201-0142</span>
        </li>
        <li class="contact-item">
          <svg class="contact-icon" viewBox="0 0 22 22"><circle cx="11" cy="11" r="11" fill="var(--icon-dark)"/><rect x="5.5" y="7" width="11" height="8" fill="#fff"/><path d="M5.5 7l5.5 4.5L16.5 7" fill="none" stroke="var(--icon-dark)" stroke-width="1.2"/></svg>
          <span>darren.holloway@kelvor.ca</span>
        </li>
        <li class="contact-item">
          <svg class="contact-icon" viewBox="0 0 22 22"><circle cx="11" cy="11" r="11" fill="var(--icon-dark)"/><circle cx="11" cy="11" r="6" fill="none" stroke="#fff" stroke-width="1.3"/><ellipse cx="11" cy="11" rx="2.6" ry="6" fill="none" stroke="#fff" stroke-width="1.1"/><line x1="5" y1="11" x2="17" y2="11" stroke="#fff" stroke-width="1.1"/></svg>
          <span>www.kelvor.ca</span>
        </li>
      </ul>
    </section>

    <div class="blue-stripe"></div>
  </article>
</main>
</body>
</html>
```